Webdesign für Software Ingenieurbüro
Vielen Dank für das professionelle Design, Umsetzung mit WordPress und rasche Reaktionszeiten. MondscheinKobold geht die Extrameile.
Zielgruppe
English text below
Meine Firma erstellt Software und bietet sämtliche Dienstleistungen rund um die Softwareentwicklung an.
Die Zielgruppe sind Auftraggeber, welche Software-Engineering/Entwicklungsaufträge vergeben.
English
My company creates software and offers all services related to software development.
The target group are those who award software engineering / development contracts.
Aufgabenstellung
Die bestehende Seite www.tarnvok-systems.ch soll neu und modern designed werden. Die Struktur der Seite (Menuunterteilung) kann (muss aber nicht zwingend) übernommen werden.
Das Logo kann, muss aber nicht übernommen werden.
Ev. als OnePage-Seite gestalten.
Responsive-Design ist zwingend, d.h. die Seite muss sowohl auf dem Desktop wie auch auf dem Mobile-Gerät ansprechend aussehen.
Zur Illustration soll auf Fotos verzichtet werden. Aber es können sehr gerne Vektorgrafiken für die Illustration und/oder Icons verwendet werden.
Link auf Social-Media Qorvu muss vorhanden sein.
Der persönliche Kontakt zum Kunden ist mir wichtig, deshalb sollte mein Foto vorhanden sein. Ev. nicht so prominent wie auf der aktuellen Seite.
Die Umsetzung wird mit Wordpress und einem Standard-Theme geschehen. Falls Sie Wordpress kennen, können Sie das Theme angeben, mit welchem sich die Seite umsetzen lässt.
The existing site www.tarnvok-systems.ch is to be redesigned and modernized. The structure of the page (menu subdivision) can (but does not have to be) mandatory.
The logo can, but does not have to be adopted.
Ev. as a OnePage page.
Responsive design is required, the page must look appealing both on the desktop and on the mobile device.
For the illustration, photographs are not desired. But vector graphics can be used for illustration and / or icons.
Link to social media Qorvu must be available.
Personal contact with the customer is important to me, so my photo should be available. Ev. not as prominent as on the current page.
The implementation will be done with Wordpress and a standard theme. If you are familiar with Wordpress, you can specify the theme with which the page can be implemented.

```html
<!DOCTYPE html>
<html lang="de">
<head>
<meta charset="utf-8">
<title>Tarnvok Systems – Projekt Arbeitsblatt</title>
<link rel="stylesheet" href="https://fonts.googleapis.com/css2?family=Roboto:ital,wght@1,300;1,400;1,700;1,900&family=Source+Sans+3:wght@300;400;600&display=swap">
<style>
:root{
  --navy-dark:#06142b;
  --navy:#0b2f5c;
  --page:#f2f3f5;
  --ink:#2a2a2a;
  --muted:#8a8a8a;
  --accent:#3a72d6;
  --white:#ffffff;
  --dot:#a9a9a9;
  --shade:rgba(0,0,0,.76);
}
*{box-sizing:border-box;margin:0;padding:0}
html,body{width:841px;height:1200px;overflow:hidden}
body{position:relative;background:var(--page);font-family:"Source Sans 3",sans-serif;color:var(--ink)}
.abs{position:absolute}
.serif-i{font-family:"Roboto",sans-serif;font-style:italic;font-weight:300}
.serif-i b{font-weight:900}

.hero{left:0;top:0;width:841px;height:305px;background:linear-gradient(120deg,var(--navy-dark) 20%,var(--navy) 100%)}
.brand{left:56px;top:14px;display:flex;align-items:center;gap:6px;color:#dfe6f0;font-size:11px;font-weight:600;line-height:1}
.brand i{width:14px;height:14px;border:2px solid #dfe6f0;border-radius:50%}
.nav{left:496px;top:22px;display:flex;gap:25px;font-size:8px;color:#c9d3e2}
.nav-sep{left:715px;top:23px;width:1px;height:8px;background:#c9d3e2}
.social{display:flex;gap:7px}
.social span{width:11px;height:11px;border:1px solid #c9d3e2}
.hero-social{left:738px;top:23px}
.hero-card{left:157px;top:249px;width:527px;height:81px;background:var(--white);border-radius:6px}

.methodik-title{left:0;width:841px;top:378px;text-align:center;font-size:19px}
.rule{width:33px;height:1px;background:var(--accent);left:404px}
.method{top:442px;width:130px;text-align:center;font-size:10.5px;line-height:12.5px;color:#555}
.method svg{display:block;margin:0 auto 21px}
.start-btn{left:372px;top:562px;width:98px;height:20px;border-radius:10px;background:var(--accent);color:#fff;font-size:7px;font-weight:600;text-align:center;line-height:20px}

.tech-card{left:165px;top:640px;width:512px;height:290px;background:var(--white);border:1px solid #e2e2e2;border-radius:12px}
.tech-inner{left:207px;top:679px;width:425px;height:251px;border-left:1px solid #ddd;border-right:1px solid #ddd}
.tech-title{left:0;width:841px;top:710px;text-align:center;font-size:17.5px;line-height:18px}
.tech-text{left:280px;width:294px;top:793px;text-align:center;font-size:8px;line-height:10.5px;color:#555}
.tech{width:80px;text-align:center;font-size:10px;font-weight:600;color:#555}
.slide-l{left:184px;top:833px;width:8px;height:8px;border:1px solid #999}
.slide-r{left:652px;top:834px;width:6px;height:6px;border-radius:50%;background:#555}

.footer{left:0;top:919px;width:841px;height:259px;background:linear-gradient(120deg,var(--navy-dark),var(--navy))}
.footer-title{left:0;width:841px;top:948px;text-align:center;font-size:17.5px;color:#fff}
.footer-text{left:225px;top:1010px;width:165px;font-size:7.5px;line-height:10.5px;color:#b9c6d8}
.footer-text p{margin-bottom:6px}
.profile{left:226px;top:1095px;font-size:8px;color:#dfe6f0}
.footer-social{left:226px;top:1116px}
.field{left:455px;width:161px;border-bottom:1px solid #b9c6d8;font-size:8px;color:#fff;height:13px}
.field-label{left:455px;font-size:4.5px;color:#9fb0c6}
.send-btn{left:479px;top:1112px;width:113px;height:20px;border-radius:10px;background:var(--accent);color:#fff;font-size:6.5px;font-weight:600;text-align:center;line-height:20px}
.copyright{left:0;top:1178px;width:841px;height:22px;background:#050c18;color:#8a97aa;font-size:5.5px;text-align:center;line-height:16px}

.shade{left:0;top:0;width:841px;height:1200px;background:var(--shade)}

.modal{left:164px;top:35px;width:513px;height:298px;background:var(--white)}
.modal-close{left:484px;top:12px}
.modal-title{left:87px;top:53px;font-size:18.5px;color:var(--accent)}
.modal-step{left:403px;top:61px;font-size:12px;color:#bbb}
.modal-step b{color:var(--accent);font-weight:400}
.question{left:88px;top:128px;font-size:12px;color:#9a9a9a;letter-spacing:.2px}
.answer{left:88px;top:160px;width:293px;height:27px;border-bottom:1px solid #444;font-size:12.5px;color:#333}
.answer sup{position:absolute;right:4px;top:0;font-size:8px;color:#999}
.steps{left:419px;top:129px;display:flex;flex-direction:column;gap:7px}
.steps i{width:6px;height:6px;border-radius:50%;background:var(--dot)}
.steps i.on{background:var(--accent)}
.next-btn{left:223px;top:207px;width:65px;height:20px;border:1.5px solid var(--accent);border-radius:10px;color:var(--accent);font-size:7px;font-weight:600;text-align:center;line-height:17px}
.hint{left:0;width:513px;top:235px;text-align:center;font-size:6px;color:#888}
</style>
</head>
<body>

<header class="abs hero"></header>
<div class="abs brand"><i></i>Tarnvok Systems</div>
<nav class="abs nav"><span>Home</span><span>Dienstleistungen</span><span>Firma</span><span>Kontakt</span></nav>
<div class="abs nav-sep"></div>
<div class="abs social hero-social"><span aria-label="Verknet"></span><span aria-label="Qorvu"></span><span aria-label="Gesichtsbuch"></span></div>
<div class="abs hero-card"></div>

<h2 class="abs methodik-title serif-i">Unsere <b>Methodik</b></h2>
<div class="abs rule" style="top:420px"></div>

<div class="abs method" style="left:157px">
  <div role="img" aria-label="Eulen-Symbol für Teamführung" style="width:30px;height:42px;margin:0 auto 21px;border-radius:12px;background:#cfdaf0"></div>
  Teamführung und Coaching
</div>
<div class="abs method" style="left:289px">
  <svg width="42" height="42" viewBox="0 0 42 42" fill="none" stroke="#3a72d6" stroke-width="2"><circle cx="24" cy="23" r="15"/><path d="M21 4h6M24 4v4M24 23l5-8M2 18h8M4 24h8M6 30h8"/></svg>
  Scrum und Extreme Programming
</div>
<div class="abs method" style="left:414px">
  <svg width="44" height="42" viewBox="0 0 44 42" fill="none" stroke="#3a72d6" stroke-width="2"><rect x="1" y="2" width="42" height="30" rx="2"/><path d="M16 38h12M22 32v6"/><rect x="26" y="18" width="12" height="22" rx="2" fill="#fff"/></svg>
  Continuous Integration/ Delivery
</div>
<div class="abs method" style="left:554px">
  <svg width="44" height="42" viewBox="0 0 44 42" fill="none" stroke="#3a72d6" stroke-width="2"><path d="M22 4v32M12 40h20M6 8h32M6 8l-5 14h10zM38 8l-5 14h10z"/><path d="M1 22a5 5 0 0 0 10 0M33 22a5 5 0 0 0 10 0"/></svg>
  Application Lifecylce Management
</div>
<div class="abs start-btn">LASS UNS START</div>

<section class="abs tech-card"></section>
<div class="abs tech-inner"></div>
<h2 class="abs tech-title serif-i"><b>Konzentrieren</b> Sie sich<br>auf <b>Technologie</b></h2>
<div class="abs rule" style="top:772px"></div>
<p class="abs tech-text">Über 18 Jahre Erfahrung in der Softwareentwicklung und Entwicklung von Backendsystemen mit hohem Transaktionsaufkommen</p>
<div class="abs slide-l"></div><div class="abs slide-r"></div>
<div class="abs tech" style="left:234px;top:844px">Kavora</div>
<div class="abs tech" style="left:332px;top:844px">Tabelix</div>
<div class="abs tech" style="left:428px;top:844px">Frühlo</div>
<div class="abs tech" style="left:525px;top:844px">Winkelis</div>
<div class="abs tech" style="left:234px;top:873px">Orakon</div>
<div class="abs tech" style="left:332px;top:873px">&lt;xml /&gt;</div>
<div class="abs tech" style="left:428px;top:873px">Ruhemo</div>
<div class="abs tech" style="left:525px;top:873px">Schaumtest</div>

<footer class="abs footer"></footer>
<h2 class="abs footer-title serif-i">Sie können eine <b>Frage stellen</b></h2>
<div class="abs rule" style="top:991px"></div>
<div class="abs footer-text">
  <p>Tarnvok Systems GmbH fokussiert sich auf die professionelle Softwareentwicklung .</p>
  <p>Ich freue mich auf Ihre Nachricht. Füllen Sie bitte untenstehendes Formular aus. Ich werde so rasch wie möglich mit Ihnen in Kontakt treten.</p>
</div>
<div class="abs profile serif-i">Besuchen Sie mein Profil: <b>Bernhard Kolmer</b></div>
<div class="abs social footer-social"><span aria-label="Verknet"></span><span aria-label="Qorvu"></span><span aria-label="Gesichtsbuch"></span></div>
<div class="abs field" style="top:1009px">Alex|</div>
<div class="abs field-label" style="top:1025px">NAME</div>
<div class="abs field" style="top:1039px"></div>
<div class="abs field-label" style="top:1055px">E-MAIL</div>
<div class="abs field" style="top:1069px"></div>
<div class="abs field-label" style="top:1087px">NACHRICHT</div>
<div class="abs send-btn">SCHICKEN NACHRICHT</div>
<div class="abs copyright">© Copyright 2010 - 2017 Tarnvok Systems GmbH. All rights reserved.</div>

<div class="abs shade"></div>

<div class="abs modal" role="dialog" aria-label="Projekt Arbeitsblatt">
  <svg class="abs modal-close" width="14" height="14" viewBox="0 0 14 14" stroke="#333" stroke-width="1.2"><path d="M1 1l12 12M13 1L1 13"/></svg>
  <h2 class="abs modal-title serif-i" style="font-weight:400">Projekt <b style="font-weight:700">Arbeitsblatt</b></h2>
  <div class="abs modal-step"><b>1</b> / 5</div>
  <div class="abs question">WIE HEIßEN SIE?</div>
  <div class="abs answer">Lotte Brenn<sup>*</sup></div>
  <div class="abs steps"><i class="on"></i><i></i><i></i><i></i><i></i></div>
  <div class="abs next-btn">WEITER</div>
  <div class="abs hint">oder drücken ENTER</div>
</div>

</body>
</html>
```